Podiatry (services) Business Card

I need a business design for a New Podiatry Service.
the Podiatry services will include all aspects of podiatry including;
general podiatry for all ages
corns and callus treatment
Ingrown toenails & nail surgery
Forefoot, arch and heel pain
Gait analysis
Sports Podiatry and Orthotics
Paediatric Assessments
Diabetes Foot Assessment

I would like the back of the card to have space for next appointment day and time.

I would like a nice design that is simple yet catchy. I don't like cluttered business cards. I like things to be simple yet stand out because of the finer details.

I like the colours blue and white but I'm open to other designs that have different colours.

Industry/Entity Type

Business

Contact Information for Business Card

Cobaltline Podiatry (Business name)

Delphine Marrow - Podiatrist
M.Pod.P., B.Hlth. Sci, MQFodE

Address: 17 Tolbrook Rd, Harlow Vale Vic, 3998
Phone: (03) 9462 3178
Fax: (03) 9514 2683

```html
<!DOCTYPE html>
<html lang="en">
<head>
<meta charset="utf-8">
<title>Cobaltline Podiatry – Business Card</title>
<link rel="stylesheet" href="https://fonts.googleapis.com/css2?family=Montserrat:wght@600&family=Merriweather:wght@300;400&family=Libre+Bodoni:wght@400&family=Oswald:wght@300&display=swap">
<style>
  :root {
    --backdrop: #cbcbcb;
    --charcoal: #4a4a4a;
    --white: #ffffff;
    --cobalt: #4183d7;
    --name-blue: #4a97d6;
    --ink: #111111;
    --soft-white: #e9e9e9;
  }
  * { margin: 0; padding: 0; box-sizing: border-box; }
  html, body { width: 1200px; height: 879px; overflow: hidden; }
  body { background: var(--backdrop); position: relative; }

  .card-front {
    position: absolute; left: 131px; top: 134px;
    width: 367px; height: 606px;
    background: var(--charcoal);
  }
  .brand {
    position: absolute; left: 51px; top: 62px;
    display: flex; align-items: flex-end; gap: 10px;
  }
  .brand-name {
    font-family: 'Montserrat', sans-serif; font-weight: 600;
    font-size: 40px; line-height: 40px; color: var(--white);
    letter-spacing: -1px;
  }
  .brand-dot {
    width: 54px; height: 54px; border: 2px solid var(--white);
    border-radius: 50%; margin-bottom: -6px;
  }
  .brand-bar {
    position: absolute; left: 51px; top: 176px;
    width: 265px; height: 24px; background: var(--white);
  }
  .person {
    position: absolute; left: 51px; top: 373px;
    font-family: 'Merriweather', serif;
  }
  .person-name { font-size: 20px; font-weight: 300; color: var(--name-blue); line-height: 26px; }
  .person-credentials { margin-top: 4px; font-size: 15.5px; font-weight: 300; color: var(--soft-white); }
  .divider {
    position: absolute; left: 50px; top: 440px;
    width: 269px; height: 2px; background: var(--white);
  }
  .contact {
    position: absolute; left: 51px; top: 463px;
    font-family: 'Merriweather', serif; font-weight: 300;
    font-size: 16.5px; line-height: 23.5px; color: var(--soft-white);
    font-style: normal;
  }

  .card-back {
    position: absolute; left: 528px; top: 237px;
    width: 615px; height: 388px; background: var(--cobalt);
    overflow: hidden;
  }
  .back-strip {
    position: absolute; left: 0; top: 0; width: 112px; height: 100%;
    background: var(--white);
  }
  .back-emblem {
    position: absolute; left: 26px; top: 104px;
    width: 184px; height: 184px; border-radius: 50%;
    background: var(--white);
    display: flex; align-items: center; justify-content: center;
  }
  .back-emblem-inner {
    width: 164px; height: 164px; border-radius: 50%;
    background: var(--charcoal);
    display: flex; align-items: center; justify-content: center;
    text-align: center;
    font-family: 'Montserrat', sans-serif; font-weight: 600;
    font-size: 17px; line-height: 21px; color: var(--white);
  }
  .appointment {
    position: absolute; left: 246px; top: 196px;
  }
  .appointment-title {
    font-family: 'Libre Bodoni', serif; font-size: 38px;
    color: var(--white); letter-spacing: 0.5px; line-height: 44px;
  }
  .appointment-field {
    display: flex; align-items: flex-end;
    font-family: 'Oswald', sans-serif; font-weight: 300;
    font-size: 33px; line-height: 40px; color: var(--ink);
    margin-top: 8px;
  }
  .appointment-field + .appointment-field { margin-top: 16px; }
  .appointment-line {
    display: inline-block; width: 218px; height: 3px;
    background: var(--ink); margin: 0 0 2px 12px;
  }
</style>
</head>
<body>
  <section class="card-front">
    <div class="brand">
      <div class="brand-name">cobaltline<br>podiatry</div>
      <div class="brand-dot"></div>
    </div>
    <div class="brand-bar"></div>
    <div class="person">
      <p class="person-name">Delphine Marrow, Podiatrist</p>
      <p class="person-credentials">M.Pod.P., B.Hlth. Sci, MQFodE</p>
    </div>
    <div class="divider"></div>
    <address class="contact">
      17 Tolbrook Rd,<br>
      Harlow Vale Vic, 3998<br>
      Phone: (03) 9462 3178<br>
      Fax: (03) 9514 2683
    </address>
  </section>

  <section class="card-back">
    <div class="back-strip"></div>
    <div class="back-emblem">
      <div class="back-emblem-inner">cobaltline<br>podiatry</div>
    </div>
    <div class="appointment">
      <p class="appointment-title">next appointment:</p>
      <p class="appointment-field">DATE:<span class="appointment-line"></span></p>
      <p class="appointment-field">TIME:<span class="appointment-line"></span></p>
    </div>
  </section>
</body>
</html>
```